Innovation Company Business Card Design

I need to have my business card updated. The current card was designed when the company started 2.5 years ago and was a quick and dirty job.

I need a new card design that is more professional and has my updated company tag line.

I will include the old card's Corel Draw file, and EPS versions as examples of the current design. I will also include the company logo eps and corel version files.

The company pantone colour is pantone 1805 c (a dark red)

I want the design to convey the nature of our business as a strategic technology innovation company, but yet still be professional. We are funky vibey and work from an industrial style office in a vibey designer dominat part of town. Though are clients include large banks and corporate clients too.

The information that needs to be on the card is in attached word document (but doesn't have to be in this order or format)

Final version needs to be supplied in PNG preview, as well as PSD file format (or other editable file version) so that personal information on card can be easily edited and reprinted.

Target Market(s)

CEO's of small to medium size companies
Marketing Managers of large coporates
Account managers of Digital Agencies

Industry/Entity Type

Business

Requirements
Must have
• 86x54mm will be cut in rounded corner credit card size format (Except if you recommend otherwise in your design)
Nice to have
• Some kind of background transparency combined with the pantone colour that gives the card some dimension and depth. But no gradient fills please :-)
Should not have
• Basic gradient fills
• Clipart

```html
<!DOCTYPE html>
<html lang="en">
<head>
<meta charset="utf-8">
<title>Velocora Business Card Options</title>
<link rel="stylesheet" href="https://fonts.googleapis.com/css2?family=Arimo:wght@400;700&family=Kalam:wght@400&family=Michroma&display=swap">
<style>
  :root {
    --board-light: #dcdcdc;
    --board-dark: #c4c4c4;
    --pantone-red: #8c0309;
    --red-1: #b8000f;
    --red-2: #b10010;
    --red-3: #a6000e;
    --logo-dark: #6a0008;
    --white: #ffffff;
    --ink: #1e1e1e;
  }
  * { margin: 0; padding: 0; box-sizing: border-box; }
  html, body { width: 1200px; height: 675px; overflow: hidden; }
  body {
    position: relative;
    background: radial-gradient(ellipse at 45% 45%, var(--board-dark) 0%, var(--board-light) 75%);
    font-family: "Arimo", Arial, sans-serif;
  }
  .option-number {
    position: absolute;
    font-family: "Michroma", sans-serif;
    font-size: 46px;
    line-height: 1;
    color: #111;
    transform: translateX(-50%) scaleX(1.35);
  }
  .card-front {
    position: absolute;
    width: 409px;
    height: 256px;
    background: var(--white);
    border-radius: 10px;
    overflow: hidden;
  }
  .card-front .texture {
    position: absolute;
    left: 0; top: 0;
    width: 100%;
    height: 228px;
  }
  .card-front .bottom-tab {
    position: absolute;
    left: 118px; top: 226px;
    width: 159px; height: 21px;
    border-radius: 0 0 3px 3px;
  }
  .card-front .top-notch {
    position: absolute;
    left: 118px; top: 0;
    width: 159px; height: 10px;
    background: var(--white);
    border-radius: 0 0 3px 3px;
  }
  .option-1 .texture, .option-1 .bottom-tab { background: var(--red-1); }
  .option-2 .texture, .option-2 .bottom-tab { background: var(--red-2); }
  .option-3 .texture, .option-3 .bottom-tab { background: var(--red-3); }
  .wordmark {
    position: absolute;
    left: 93px; top: 108px;
    width: 240px;
    text-align: right;
    color: var(--white);
  }
  .wordmark .company-name {
    display: block;
    text-align: center;
    font-weight: 700;
    font-size: 44px;
    line-height: 44px;
    letter-spacing: -0.5px;
  }
  .wordmark .tagline {
    display: block;
    font-size: 12px;
    line-height: 14px;
    margin-right: 6px;
  }
  .option-3 .wordmark { color: var(--logo-dark); }

  .card-back {
    position: absolute;
    left: 652px; top: 363px;
    width: 462px; height: 289px;
    background: var(--white);
    border-radius: 12px;
    overflow: hidden;
  }
  .card-back .brand-panel {
    position: absolute;
    left: 0; top: 0;
    width: 279px; height: 100%;
    background: var(--pantone-red);
  }
  .card-back .side-tab {
    position: absolute;
    left: 278px; top: 47px;
    width: 12px; height: 187px;
    background: var(--pantone-red);
    border-radius: 0 4px 4px 0;
  }
  .card-back .side-slot {
    position: absolute;
    left: 0; top: 52px;
    width: 15px; height: 184px;
    background: var(--white);
    border-radius: 0 4px 4px 0;
  }
  .card-back .panel-name {
    position: absolute;
    left: 20px; top: 80px;
    width: 259px;
    text-align: center;
    font-weight: 700;
    font-size: 34px;
    color: var(--white);
  }
  .card-back .person-name {
    position: absolute;
    left: 40px; top: 138px;
    width: 220px;
    text-align: right;
    font-family: "Kalam", cursive;
    font-size: 30px;
    line-height: 36px;
    color: var(--white);
  }
  .card-back .person-role {
    position: absolute;
    left: 40px; top: 173px;
    width: 220px;
    text-align: right;
    font-size: 12px;
    letter-spacing: 3.2px;
    color: var(--white);
  }
  .contact-list {
    position: absolute;
    left: 294px; top: 86px;
    list-style: none;
    color: var(--ink);
    font-size: 13px;
    letter-spacing: 1px;
  }
  .contact-list li { line-height: 23px; }
  .contact-list li.gap { line-height: 18px; }
  .company-block {
    position: absolute;
    left: 294px; top: 173px;
    color: var(--ink);
  }
  .company-block .legal-name { font-size: 12px; line-height: 15px; letter-spacing: 0.3px; }
  .company-block .address { font-size: 8px; line-height: 9px; letter-spacing: 0.1px; }
</style>
</head>
<body>
  <span class="option-number" style="left:242px; top:6px;">1</span>
  <span class="option-number" style="left:682px; top:6px;">2</span>
  <span class="option-number" style="left:259px; top:339px;">3</span>

  <div class="card-front option-1" style="left:53px; top:52px;">
    <div class="texture" role="img" aria-label="Fine woven red fabric texture"></div>
    <div class="bottom-tab"></div>
    <div class="top-notch"></div>
    <div class="wordmark">
      <span class="company-name">Velocora</span>
      <span class="tagline">Strategic Innovation</span>
    </div>
  </div>

  <div class="card-front option-2" style="left:490px; top:52px;">
    <div class="texture" role="img" aria-label="Red rippling water caustics texture"></div>
    <div class="bottom-tab"></div>
    <div class="top-notch"></div>
    <div class="wordmark">
      <span class="company-name">Velocora</span>
      <span class="tagline">Strategic Innovation</span>
    </div>
  </div>

  <div class="card-front option-3" style="left:53px; top:388px;">
    <div class="texture" role="img" aria-label="Deep red rippling water caustics texture"></div>
    <div class="bottom-tab"></div>
    <div class="top-notch"></div>
    <div class="wordmark">
      <span class="company-name">Velocora</span>
      <span class="tagline">Strategic Innovation</span>
    </div>
  </div>

  <div class="card-back">
    <div class="brand-panel"></div>
    <div class="side-tab"></div>
    <div class="side-slot"></div>
    <div class="panel-name">Velocora</div>
    <div class="person-name">Daniel Marsh</div>
    <div class="person-role">Founder &amp; MD</div>
    <ul class="contact-list">
      <li>0741286390</li>
      <li>021 487 3365</li>
      <li class="gap">www.velocora.com</li>
      <li class="gap">daniel@velocora.com</li>
    </ul>
    <div class="company-block">
      <div class="legal-name">Velocora (Pty) Ltd</div>
      <div class="address">UNIT 204, 18 HARBOURVIEW AVE.<br>NORTHCLIFF, CPT, RSA</div>
    </div>
  </div>
</body>
</html>
```